Lucien business card

Business card for commercial photography , photographer specialized in advertising, architecture and interior photography, adventure imagery and camera work. 40 years old, worked for the last 20 years. Business card needs to convey a sense of confidence in work achieved. Card needs to be eye catching as will be left behind in many people's offices. Should also mention discreetly NRVB accredited photographer at the verso of the card. Phone number and website link must be apparent easily.

Target Market(s)

Advertising agencies, commercial photography representation

Industry/Entity Type

Architecture

Contact Information for Business Card

Phone number : +61 470 918 264
lucien.marvaux@velmora.example
www.lucienmarvaux.example

Font styles to use
Sans Serif

Requirements
Must have
• Email adress
• Website
• Phone number
• Name
• Photographer
Nice to have
• NRVB accredited photographer
Should not have
• Rond corners

```html
<!DOCTYPE html>
<html lang="en">
<head>
<meta charset="utf-8">
<title>Lucien business card</title>
<link rel="stylesheet" href="https://fonts.googleapis.com/css2?family=Oswald:wght@400;500;700&display=swap">
<style>
  :root {
    --page: #222222;
    --card-dark: #121212;
    --card-mid: #1e1e1e;
    --yellow: #ffe600;
    --orange: #f7791f;
    --white: #ffffff;
    --ink: #1a1a1a;
  }
  * { margin: 0; padding: 0; box-sizing: border-box; }
  html, body {
    width: 840px; height: 1200px; overflow: hidden;
    background: var(--page);
    font-family: "Oswald", "Arial Narrow", sans-serif;
  }
  .canvas { position: relative; width: 840px; height: 1200px; }

  .card {
    position: absolute; left: 108px; width: 624px; height: 378px;
    background:
      radial-gradient(ellipse at 40% 35%, var(--card-mid) 0%, var(--card-dark) 70%),
      var(--card-dark);
    overflow: hidden;
  }
  .card-front { top: 215px; }
  .card-back { top: 607px; }

  /* Front */
  .name-rule {
    position: absolute; left: 0; width: 453px; height: 3px;
    background: var(--yellow);
  }
  .name-rule.top { top: 110px; }
  .name-rule.bottom { top: 274px; }
  .name {
    position: absolute; left: 26px; top: 118px;
    color: var(--yellow); font-weight: 700;
    font-size: 84px; line-height: 0.83; letter-spacing: 1px;
    text-transform: uppercase;
  }
  .accreditation {
    position: absolute; left: 208px; top: 320px; width: 416px; height: 35px;
    background: var(--orange);
    display: flex; align-items: center; padding-left: 10px;
    font-weight: 500; font-size: 21px; letter-spacing: 1.6px;
    color: #ffe98a; text-transform: uppercase; white-space: nowrap;
  }
  .accreditation .body-name { color: var(--white); margin-right: 8px; font-weight: 700; }

  /* Back */
  .contact-row {
    position: absolute; left: 0; top: 110px; width: 624px; height: 116px;
    display: flex;
  }
  .contact {
    flex: 1; display: flex; flex-direction: column; align-items: center;
    justify-content: flex-end; padding-bottom: 14px; gap: 18px;
    color: var(--ink); font-size: 18px; letter-spacing: 0.8px;
  }
  .contact.phone { background: var(--orange); }
  .contact.email { background: var(--yellow); font-size: 16px; letter-spacing: 0.4px; }
  .contact svg { display: block; }
  .web-band {
    position: absolute; left: 0; top: 226px; width: 624px; height: 59px;
    background: var(--white);
    display: flex; align-items: center; padding-left: 42px; gap: 14px;
    color: var(--ink); font-size: 36px; letter-spacing: 2px;
  }
</style>
</head>
<body>
<div class="canvas">
  <section class="card card-front">
    <div class="name-rule top"></div>
    <h1 class="name">Lucien<br>Marvaux</h1>
    <div class="name-rule bottom"></div>
    <p class="accreditation"><span class="body-name">NRVB</span>Accredited Photographer</p>
  </section>

  <section class="card card-back">
    <div class="contact-row">
      <div class="contact phone">
        <svg width="22" height="40" viewBox="0 0 22 40" aria-hidden="true">
          <rect x="13" y="0" width="3" height="7" fill="#1a1a1a"/>
          <rect x="2" y="6" width="18" height="33" rx="2" fill="#1a1a1a"/>
          <rect x="5" y="10" width="12" height="9" fill="#f7791f"/>
          <g fill="#f7791f">
            <rect x="5" y="23" width="3" height="3"/><rect x="9.5" y="23" width="3" height="3"/><rect x="14" y="23" width="3" height="3"/>
            <rect x="5" y="28" width="3" height="3"/><rect x="9.5" y="28" width="3" height="3"/><rect x="14" y="28" width="3" height="3"/>
            <rect x="5" y="33" width="3" height="3"/><rect x="9.5" y="33" width="3" height="3"/><rect x="14" y="33" width="3" height="3"/>
          </g>
        </svg>
        <span>+61 470 918 264</span>
      </div>
      <div class="contact email">
        <svg width="50" height="32" viewBox="0 0 50 32" aria-hidden="true">
          <rect x="0" y="0" width="50" height="32" fill="#1a1a1a"/>
          <polyline points="3,3 25,19 47,3" fill="none" stroke="#ffe600" stroke-width="3"/>
          <line x1="3" y1="29" x2="19" y2="15" stroke="#ffe600" stroke-width="3"/>
          <line x1="47" y1="29" x2="31" y2="15" stroke="#ffe600" stroke-width="3"/>
        </svg>
        <span>lucien.marvaux@velmora.example</span>
      </div>
    </div>
    <div class="web-band">
      <svg width="40" height="40" viewBox="0 0 40 40" aria-hidden="true" fill="none" stroke="#1a1a1a" stroke-width="2.6">
        <circle cx="20" cy="20" r="17.5"/>
        <ellipse cx="20" cy="20" rx="7.5" ry="17.5"/>
        <line x1="20" y1="2.5" x2="20" y2="37.5"/>
        <line x1="2.5" y1="20" x2="37.5" y2="20"/>
        <path d="M5.5 11 H34.5 M5.5 29 H34.5"/>
      </svg>
      <span>www.lucienmarvaux.example</span>
    </div>
  </section>
</div>
</body>
</html>
```